Luxury Bath Flyer

I would like to have a professional Flyer, which would describe a beautiful atmospheric luxury-Bath situation. I am sending you a( screenshot) Flyer Proposal, which shoes my intention and wish how I would like to have it. Please note that Ästhetik and a professional Flyer is very important to me. If possible send a psd.file or a indesign file, in case of we gonna need to change the text. You are also free to make 2 different proposals and one as you would suggest.?(I send you couple pictures, but the main one which I choose on the pdf file, please keep that, it is called " KR-71" - If there is a question please let me know. Looking forward to receive an amazing artwork.Kind Regards Merle
Look and feel
Each slider illustrates characteristics of the customer's brand and the style your logo design should communicate.

```html
<!DOCTYPE html>
<html lang="de">
<head>
<meta charset="utf-8">
<title>Wohnwerk – Bad zum Fixpreis</title>
<link href="https://fonts.googleapis.com/css2?family=Open+Sans:wght@400;600;700&family=Great+Vibes&display=swap" rel="stylesheet">
<style>
:root{
  --blue:#0b4aa2;
  --blue-bright:#1a7fd0;
  --orange:#e5400e;
  --ink:#1c1c1c;
  --grey-band:#dcdcdc;
  --frame:#8f8f8f;
  --white:#ffffff;
}
*{margin:0;padding:0;box-sizing:border-box}
html,body{width:880px;height:1200px;overflow:hidden;background:var(--white)}
body{font-family:"Open Sans",Arial,sans-serif;color:var(--ink)}
.flyer{position:relative;width:880px;height:1200px;overflow:hidden;background:var(--white)}
.abs{position:absolute}

.brand{left:39px;top:40px;display:flex;align-items:center;gap:12px}
.brand-mark{width:22px;height:22px;background:var(--ink)}
.brand-name{font-weight:700;font-size:34px;color:var(--ink);letter-spacing:-.5px}
.tagline{left:228px;top:84px;font-size:17px;line-height:24px;font-weight:600;color:var(--ink)}
.tagline .bad{color:var(--blue)}
.tagline .heat{color:var(--orange)}

.stripe{left:0;top:0;width:880px;height:520px}
.hero-frame{left:413px;top:26px;width:442px;height:484px;background:#9a9a9a;padding:12px}
.hero-photo{width:100%;height:100%;background:linear-gradient(160deg,#e9ebec 0%,#cfd3d4 35%,#a89b8a 60%,#8a7e72 100%)}

.ihr{left:40px;top:200px;font-size:36px;color:var(--orange);font-weight:400}
.exklusiv{left:70px;top:238px;font-family:"Great Vibes",cursive;font-size:74px;color:var(--blue);line-height:1}
.fixpreis{left:40px;top:320px;font-size:32px}
.fixpreis b{color:var(--orange);font-weight:600}
.claim{left:42px;top:378px;font-size:27px;line-height:39px}
.claim .hand{color:var(--blue);font-weight:600}

.section-tab{left:253px;width:374px;height:39px;background:var(--blue);color:var(--white);font-weight:700;font-size:23px;text-align:center;line-height:39px;box-shadow:0 8px 8px -6px rgba(0,0,0,.45);z-index:2}
.services{left:0;top:551px;width:880px;height:171px;background:var(--orange)}
.service{position:absolute;top:36px;width:210px;text-align:center;color:var(--white);font-size:18px;font-weight:600;line-height:25px}
.service svg{display:block;margin:0 auto 14px;width:64px;height:64px}

.perks{left:0;top:722px;width:880px;height:319px;background:var(--grey-band)}
.perk-list{position:absolute;top:78px;left:0;width:880px;display:flex;justify-content:center;gap:22px;font-size:18px;font-weight:600}
.perk-list span{display:flex;align-items:center;gap:8px}
.perk-list svg{width:16px;height:16px}
.rule{position:absolute;top:124px;height:3px;width:324px}
.rule.left{left:85px;background:linear-gradient(90deg,transparent,var(--orange))}
.rule.right{left:469px;background:linear-gradient(90deg,var(--orange),transparent)}
.thumb{position:absolute;top:145px;width:196px;height:128px;background:#8c8c8c;padding:8px}
.thumb div{width:100%;height:100%}

.contact-row{left:0;top:1082px;width:880px;height:50px}
.phone{position:absolute;left:52px;top:4px;display:flex;align-items:center;gap:10px;font-size:35px;font-weight:600}
.phone svg{width:30px;height:30px}
.divider{position:absolute;top:0;width:3px;height:50px;background:linear-gradient(180deg,#fff,#999,#fff)}
.addr,.web{position:absolute;top:0;font-size:18px;line-height:25px}
.addr{left:346px}
.web{left:615px}
.line{display:flex;align-items:center;gap:10px}
.line svg{width:16px;height:16px;flex:none}
.follow{left:0;top:1144px;width:880px;display:flex;justify-content:center;align-items:center;gap:18px;font-size:23px;font-weight:600;padding-left:40px}
.social{width:30px;height:30px;border:2px solid var(--orange);border-radius:50%;background:var(--white)}
.follow .label{margin-right:6px}
</style>
</head>
<body>
<div class="flyer">

  <svg class="abs stripe" viewBox="0 0 880 520" aria-hidden="true">
    <polygon points="0,150 413,262 413,277 0,166" fill="var(--blue-bright)"/>
    <polygon points="855,382 880,389 880,400 855,394" fill="var(--blue-bright)"/>
  </svg>

  <div class="abs brand"><span class="brand-mark"></span><span class="brand-name">Wohnwerk</span></div>
  <div class="abs tagline">WIR MACHEN<br><span class="bad">BAD</span> <span class="heat">HEIZUNG</span><br>UND MEHR!</div>

  <div class="abs hero-frame"><div class="hero-photo" role="img" aria-label="Foto eines modernen Badezimmers mit Holzwaschtisch, Mosaikwand und freistehender Wanne"></div></div>

  <div class="abs ihr">Ihr</div>
  <div class="abs exklusiv">Exklusives</div>
  <div class="abs fixpreis">Bad zum <b>Fixpreis!</b></div>
  <div class="abs claim">Wir montieren für Sie…<br>und das<br><span class="hand">„Alles aus einer Hand“!</span></div>

  <div class="abs section-tab" style="top:528px">Unsere Services</div>
  <div class="abs services">
    <div class="service" style="left:31px">
      <svg viewBox="0 0 64 64" fill="none" stroke="#fff" stroke-width="3" stroke-linejoin="round"><path d="M34 6h22v22L28 56 6 34z"/><circle cx="46" cy="16" r="4"/></svg>
      Markenbäder zum<br>Online Preis
    </div>
    <div class="service" style="left:216px">
      <svg viewBox="0 0 64 64" fill="none" stroke="#fff" stroke-width="3"><rect x="12" y="12" width="40" height="40" rx="4"/><path d="M32 12v40M12 32h40"/></svg>
      Wir montieren<br>für Sie
    </div>
    <div class="service" style="left:413px">
      <svg viewBox="0 0 64 64" fill="none" stroke="#fff" stroke-width="3"><circle cx="32" cy="32" r="20"/><circle cx="32" cy="32" r="8"/><path d="M32 4v8M32 52v8M4 32h8M52 32h8M12 12l6 6M46 46l6 6M52 12l-6 6M18 46l-6 6"/></svg>
      Funktionalität<br>und Ästhetik
    </div>
    <div class="service" style="left:621px">
      <svg viewBox="0 0 64 64" fill="none" stroke="#fff" stroke-width="3"><path d="M14 20a10 10 0 1 1 12 10v8h-8v-8a10 10 0 0 1-4-10z"/><path d="M18 44h8"/><circle cx="44" cy="28" r="7"/><circle cx="56" cy="22" r="4"/></svg>
      Komplettlösungen mit<br>rasche Umsetzung
    </div>
  </div>

  <div class="abs perks">
    <div class="perk-list">
      <span><svg viewBox="0 0 16 16" fill="none" stroke="var(--blue)" stroke-width="1.6"><circle cx="8" cy="8" r="6.5"/><path d="M5 8l2 2 4-4"/></svg>Individuelle Badplanung</span>
      <span><svg viewBox="0 0 16 16" fill="none" stroke="var(--blue)" stroke-width="1.6"><circle cx="8" cy="8" r="6.5"/><path d="M5 8l2 2 4-4"/></svg>Eigene Handwerker vor Ort</span>
      <span><svg viewBox="0 0 16 16" fill="none" stroke="var(--blue)" stroke-width="1.6"><circle cx="8" cy="8" r="6.5"/><path d="M5 8l2 2 4-4"/></svg>Traumbad erlebniss</span>
    </div>
    <div class="rule left"></div>
    <div class="rule right"></div>
    <div class="thumb" style="left:27px"><div role="img" aria-label="Foto eines Aufsatzwaschbeckens vor rosafarbener Wand" style="background:linear-gradient(135deg,#b07870,#d8c8c0 60%,#6f6a66)"></div></div>
    <div class="thumb" style="left:237px"><div role="img" aria-label="Foto eines Bades mit Holzmöbeln und freistehender Wanne" style="background:linear-gradient(135deg,#e6e2dc,#b9a68f 55%,#5a4a3c)"></div></div>
    <div class="thumb" style="left:447px"><div role="img" aria-label="Foto eines Waschtisches vor Mosaikwand mit Blumen" style="background:linear-gradient(160deg,#d9c7b2,#f2efe9 55%,#9b8067)"></div></div>
    <div class="thumb" style="left:657px"><div role="img" aria-label="Foto eines Schauraums mit Badkojen und Heizkörpern" style="background:linear-gradient(135deg,#3b3a3a,#cfcfcf 50%,#4a4340)"></div></div>
  </div>

  <div class="abs section-tab" style="top:1020px">Kontaktiere uns</div>

  <div class="abs contact-row">
    <div class="phone">
      <svg viewBox="0 0 30 30" fill="none" stroke="var(--blue)" stroke-width="2.2"><circle cx="15" cy="15" r="13"/><path d="M10 8l3 3-2 2c1 2 3 4 5 5l2-2 3 3-2 3c-5 0-11-6-11-11z" fill="var(--blue)" stroke="none"/></svg>
      0800 046 918
    </div>
    <div class="divider" style="left:322px"></div>
    <div class="addr">
      <div class="line"><svg viewBox="0 0 16 16" fill="none" stroke="var(--blue)" stroke-width="1.4"><path d="M8 15s5-5 5-9A5 5 0 0 0 3 6c0 4 5 9 5 9z"/><circle cx="8" cy="6" r="1.8"/></svg>Lindenstraße 12,</div>
      <div class="line"><span style="width:16px"></span>2351 Au am Feld</div>
    </div>
    <div class="divider" style="left:596px"></div>
    <div class="web">
      <div class="line"><svg viewBox="0 0 16 16" fill="none" stroke="var(--blue)" stroke-width="1.4"><rect x="1.5" y="3.5" width="13" height="9"/><path d="M1.5 3.5l6.5 5 6.5-5"/></svg>office@wohnwerk-bad.at</div>
      <div class="line"><svg viewBox="0 0 16 16" fill="none" stroke="var(--blue)" stroke-width="1.4"><circle cx="8" cy="8" r="6.5"/><path d="M1.5 8h13M8 1.5c-3 3.5-3 9.5 0 13M8 1.5c3 3.5 3 9.5 0 13"/></svg>www.wohnwerk-bad.at</div>
    </div>
  </div>

  <div class="abs follow">
    <span class="label">Folgen Sie uns</span>
    <span class="social"></span><span class="social"></span><span class="social"></span><span class="social"></span><span class="social"></span>
  </div>

</div>
</body>
</html>
```